QV - menu design

Hi,

We require elegant menu design for upscale restaurant. Please find attached the logo and the menu items for your reference.

for inspiration, this is a good website: -
http://www.platewhisper.example/bellfoldnotes/about.php

We are very much open for Menu Size suggestions.

unfortunately the place is going under renovation, we don't have updated images to it. the closest look and feel to our place is http://varnelo.example ..

we are also open for creative options on the shape, the styles, etc. as long as it represents the fine dine feel ...

Thanks ...

Dear All,

We wouldlike to extend our apology for not being able to provide feedbacks on everysingle design. We were extremely busy and we have multiple contests opensimultaneously which makes the process even harder.

However,we would like to thank you all for the efforts you have put into designingour menu. It is very much appreciated …

We wishyou all success in your design ventures and we are quite positive that we willbe working with many of you on many projects in the soon future. 

Thanks & Regards,

TLG Team...

 

 

 

Industry/Entity Type

Restaurant

Requirements
Must have
• Please ensure that there are 'some' images in the menu ... this is very important.
Should not have
• IMPORTANT: -

1. Please DO NOT insert any currency sign to the menu
2. Please keep the prices of the menu at the end of the menu items descriptions NOT beside the menu item names. The font of the price should be similar to the menu item description and please DO NOT bold the numbers. the prices should be subtle.

Thank you ...

```html
<!DOCTYPE html>
<html lang="en">
<head>
<meta charset="utf-8">
<title>Quill Vale Café — Menu</title>
<link rel="stylesheet" href="https://fonts.googleapis.com/css2?family=Barlow:wght@600&display=swap">
<style>
  :root {
    --cover-bg: #151618;
    --accent-line: #a5805d;
    --ink-light: #ffffff;
  }
  html, body {
    margin: 0;
    padding: 0;
    width: 768px;
    height: 1200px;
    overflow: hidden;
    background: var(--cover-bg);
  }
  .menu-cover {
    position: relative;
    width: 768px;
    height: 1200px;
    background: var(--cover-bg);
    font-family: "Barlow", "Helvetica Neue", Arial, sans-serif;
  }
  .cover-lines {
    position: absolute;
    inset: 0;
  }
  .cover-lines polyline {
    fill: none;
    stroke: var(--accent-line);
    stroke-width: 1.2;
  }
  .brand-name {
    position: absolute;
    left: 0;
    width: 768px;
    top: 482px;
    margin: 0;
    text-align: center;
    color: var(--ink-light);
    font-weight: 600;
    font-size: 30px;
    letter-spacing: 0.22em;
    line-height: 1;
    padding-left: 0.22em;
    box-sizing: border-box;
    text-transform: uppercase;
  }
  .cover-title {
    position: absolute;
    left: 0;
    width: 768px;
    top: 1072px;
    margin: 0;
    text-align: center;
    color: var(--ink-light);
    font-weight: 600;
    font-size: 28px;
    letter-spacing: 0.2em;
    padding-left: 0.2em;
    box-sizing: border-box;
    line-height: 1;
  }
</style>
</head>
<body>
  <main class="menu-cover">
    <svg class="cover-lines" width="768" height="1200" viewBox="0 0 768 1200" aria-hidden="true">
      <polyline points="768,128 495,462 443,462"/>
      <polyline points="0,818 224,543 457,543"/>
    </svg>
    <h1 class="brand-name">Quill Vale Café</h1>
    <p class="cover-title">MENU</p>
  </main>
</body>
</html>
```